Logo & Graphic Design for Children's Event

We need help designing the logo and marketing materials for our summer children's event "Star Parade". This program is for children ages 5-10 and should have a bold, fun feel to it. I would like a strong logo that is the primary feature of the design with additional supporting artwork elements that can be used flexibly in a variety of formats and mediums. I would like the design to capture the overall feel of the event. This event will be themed like a TV game show/variety show and should reflect this vibe.

This design will be used for outside marketing and branding and needs to be provided in a vector format. The types of mediums it would be used on is yard signs, banners, door hangers, social media, etc. (Samples of materials from previous events included in the uploaded files to help you get a feel for the quality and tone that we aim for with this event.)

Target Market(s)

Families with children ages 5-10

Industry/Entity Type

Church

Requirements
Must have
• - Strong logo that communicates the feel of the event and includes the name "Star Parade". - Flexible supporting artwork elements that can be used in a variety of mediums. - Must use fonts that are available from free, open sources or can be provided upon delivery of completed project. - Must be kid and family friendly - Event date June 10-14 must be included - Event time 6:30-8:30pm included - Include our church logo attached - Event web address Brightpathmeadow.com/KDC
Nice to have
• - A themed background that could be adapted for use on powerpoint.
Should not have
• - Any content that is scary, violent or not suitable for an audience of children.

```html
<!DOCTYPE html>
<html lang="en">
<head>
<meta charset="UTF-8">
<title>Star Parade – Summer Kids Event</title>
<link rel="stylesheet" href="https://fonts.googleapis.com/css2?family=Cinzel:wght@500;600;700&family=Marcellus&family=Rye&display=swap">
<style>
  :root {
    --ink: #111111;
    --red: #ed1c24;
    --paper: #ffffff;
    --muted: #3d3d3d;
  }
  html, body {
    margin: 0;
    padding: 0;
    width: 1200px;
    height: 1200px;
    overflow: hidden;
    background: var(--paper);
  }
  .poster {
    position: relative;
    width: 1200px;
    height: 1200px;
    background: var(--paper);
    color: var(--ink);
    font-family: "Cinzel", serif;
  }
  .headline {
    position: absolute;
    top: 124px;
    left: 0;
    width: 1200px;
    text-align: center;
    font-size: 46px;
    font-weight: 600;
    letter-spacing: 0.09em;
    margin: 0;
  }
  .frame {
    position: absolute;
    left: 0;
    top: 0;
  }
  .title {
    position: absolute;
    left: 0;
    top: 236px;
    width: 1200px;
    margin: 0;
    text-align: center;
  }
  .title__star {
    display: block;
    font-family: "Rye", serif;
    font-weight: 400;
    font-size: 176px;
    line-height: 1;
    letter-spacing: 0.04em;
    color: var(--red);
    height: 254px;
    padding-top: 18px;
    box-sizing: border-box;
  }
  .title__parade {
    display: block;
    font-family: "Cinzel", serif;
    font-size: 130px;
    font-weight: 700;
    line-height: 1;
    letter-spacing: 0.06em;
    padding-left: 0.06em;
  }
  .details {
    position: absolute;
    left: 0;
    width: 1200px;
    text-align: center;
    margin: 0;
    font-size: 30px;
    font-weight: 500;
    letter-spacing: 0.42em;
    padding-left: 0.42em;
    box-sizing: border-box;
  }
  .details--date { top: 670px; }
  .details--time { top: 742px; }
  .church {
    position: absolute;
    left: 412px;
    top: 910px;
    display: flex;
    align-items: center;
    gap: 10px;
  }
  .church__dot {
    width: 116px;
    height: 116px;
    border-radius: 50%;
    background: var(--ink);
  }
  .church__name {
    font-family: "Cinzel", serif;
    font-weight: 700;
    color: var(--ink);
    line-height: 1;
  }
  .church__name-main { display: block; font-size: 29px; }
  .church__name-sub { display: block; font-size: 15px; letter-spacing: 0.06em; margin-top: 6px; }
  .web {
    position: absolute;
    top: 1054px;
    left: 0;
    width: 1200px;
    text-align: center;
    margin: 0;
    font-size: 28px;
    font-weight: 700;
  }
  .contact {
    position: absolute;
    top: 1126px;
    left: 0;
    width: 1200px;
    display: flex;
    justify-content: center;
    gap: 22px;
    font-family: "Marcellus", serif;
    font-size: 22px;
    color: var(--muted);
  }
  .contact__sep {
    width: 2px;
    height: 30px;
    background: var(--muted);
    align-self: center;
  }
</style>
</head>
<body>
  <main class="poster">
    <h2 class="headline">Mark Your Summer Calendars</h2>

    <svg class="frame" width="1200" height="1200" viewBox="0 0 1200 1200" aria-hidden="true">
      <g fill="var(--ink)">
        <rect x="184" y="380" width="92" height="12"/>
        <rect x="924" y="380" width="84" height="12"/>
        <rect x="184" y="380" width="12" height="696"/>
        <rect x="996" y="380" width="12" height="696"/>
        <rect x="184" y="1064" width="80" height="12"/>
        <rect x="926" y="1064" width="82" height="12"/>
      </g>
    </svg>

    <h1 class="title">
      <span class="title__star">STAR</span>
      <span class="title__parade">PARADE</span>
    </h1>

    <p class="details details--date">DATE: JUNE 10-14</p>
    <p class="details details--time">EVENT TIME: 6:30-8:30PM</p>

    <div class="church">
      <span class="church__dot"></span>
      <span class="church__name">
        <span class="church__name-main">MEADOWLIGHT</span>
        <span class="church__name-sub">COMMUNITY CHURCH</span>
      </span>
    </div>

    <p class="web">WWW.BRIGHTPATHMEADOW.COM/KDC</p>

    <div class="contact">
      <span>INFO@BRIGHTPATHMEADOW.COM</span>
      <span class="contact__sep"></span>
      <span>555-014-2837</span>
      <span class="contact__sep"></span>
      <span>1450 ORCHARD LANE FAIRVIEW KS, 66000</span>
    </div>
  </main>
</body>
</html>
```